Buchcover-Design für Detoxkur
Vielen lieben Dank für die professionelle Zusammenarbeit, die sich auch im zweiten Projekt erfolgreich bestätigen ließ. Tip Top! Dankeschön!!!!
Zielgruppe
Ich bin Gesundheits- und Ernährungsberater und suche nach einem Buchcover für mein neues Projekt (Taschenbuch und E-Book) Meine Zielgruppe sind Menschen die auf der Suche nach Heilung und mehr Wohlbefinden sind. (Detoxkur-Entschlacken und Entgiften etc....)
Aufgabenstellung
Das Design sollte durch den Titel deutlich auffallen. Vorzugsweise ein dunkler Hintergrund, Titel in großer Schrift. Eingearbeitet etwas Gemüse und Obst, grüner Saft oder auch ein Smoothie, Zitronenwasser, Magen- und Darmtrakt oder ähnlichem. Es darf auch verspielt sein aber dennoch Niveauvoll.
Das Buch einschließlich Titel und Untertitel, sowie Klappentext werden derzeit von einem Lektor bearbeitet, also können diesbezüglich noch leichte Änderungen anfallen die dann anzupassen wären.
Das Buchformat ist 12cm x 19cm. Die Endgültigen Abmaße müssten nach dem Buchindesign noch angepasst werden, wenn die Seitenzahlen feststehen.
Würde gerne den Coverdesigner im Impressum des Buchs erwähnen und Bitte darum um Einverständnis, wenn es auch erwünscht sein sollte!
Derzeitiger Text :
Titel: Morgenlicht - Finde Ruhe durch Wandern und Tagträumen
Untertitel: - Durch Entgiften und Entschlacken das Wohlbefinden steigern, die Darmgesundheit wieder herstellen, das Gewicht reduzieren und die Heilung für Körper und Geist einleiten -
Klappentext: Bist du auf der Suche nach mehr Wohlbefinden und möchtest deine Gesundheit nachhaltig verbessern? Suchst du nach Methoden deinen Körper von Schadstoffen zu befreien, die dich in der Vergangenheit belastet haben? Möglicherweise fragst du dich warum das so ist und was es damit auf sich hat?
Detox, Entschlacken und Entgiften, Diäten und eine gesündere Ernährungsweise ist in aller Munde. Der Grund dafür ist bei zahlreichen Menschen ein mangelndes Wohlbefinden durch zivillisationsbedingte Einflüsse wie Umweltverschmutzungen, Stress und eine unbewusste Ernährungsweise. Diese Faktoren führen zu krankhaften Symptomen, Energie- und Antriebslosigkeit und letztendlich zu den steigenden Zahlen übergewichtiger Menschen in unserer Bevölkerung.
In diesem Ratgeber erfährst du, wie wichtig es ist sich zu entgiften und wie wichtig dafür eine gesunde Ernähru..

```html
<!DOCTYPE html>
<html lang="de">
<head>
<meta charset="utf-8">
<title>Morgenlicht – Buchcover</title>
<link rel="stylesheet" href="https://fonts.googleapis.com/css2?family=Archivo+Black&family=Roboto:wght@400;500;700&family=Roboto+Condensed:wght@400&display=swap">
<style>
  :root{
    --paper:#f3f4f3;
    --ink:#13202a;
    --spine:#0f1c21;
    --box:#0f1d22;
    --green:#7ec70f;
    --light:#d5dadc;
    --white:#ffffff;
  }
  html,body{margin:0;padding:0;overflow:hidden;}
  body{width:1200px;height:877px;background:var(--paper);font-family:'Roboto',sans-serif;}
  .wrap{position:relative;width:1200px;height:877px;overflow:hidden;}

  /* back cover */
  .back{position:absolute;left:0;top:0;width:553px;height:877px;background:var(--paper);}
  .fruit-top{position:absolute;left:0;top:0;width:553px;height:165px;
    background:linear-gradient(180deg,rgba(150,40,60,.55) 0%,rgba(230,150,40,.35) 40%,rgba(243,244,243,0) 100%);}
  .fruit-bottom{position:absolute;left:0;bottom:0;width:553px;height:135px;
    background:linear-gradient(0deg,rgba(90,130,40,.8) 0%,rgba(200,120,40,.45) 55%,rgba(243,244,243,0) 100%);}
  .back-title{position:absolute;left:0;width:553px;top:132px;text-align:center;
    font-family:'Archivo Black',sans-serif;font-size:52px;color:var(--green);letter-spacing:1px;margin:0;line-height:1;}
  .back-subtitle{position:absolute;left:0;width:553px;top:210px;text-align:center;margin:0;
    font-weight:700;font-size:24px;line-height:30px;color:var(--ink);letter-spacing:.5px;}
  .blurb{position:absolute;left:30px;top:281px;width:488px;color:var(--ink);font-size:16px;line-height:19.5px;letter-spacing:.55px;}
  .blurb p{margin:0 0 19.5px;}

  /* spine */
  .spine{position:absolute;left:553px;top:0;width:95px;height:877px;background:var(--spine);}
  .spine-text{position:absolute;left:47px;top:441px;transform:translate(-50%,-50%) rotate(-90deg);
    white-space:nowrap;font-size:17.2px;letter-spacing:1px;color:var(--white);}
  .spine-text .spine-title{color:var(--green);}

  /* front cover */
  .front{position:absolute;left:648px;top:0;width:552px;height:877px;background:var(--paper);}
  .author{position:absolute;left:0;width:552px;top:30px;text-align:center;margin:0;
    font-size:30px;font-weight:400;color:var(--ink);letter-spacing:1px;}
  .produce{position:absolute;left:18px;top:85px;width:520px;height:675px;border-radius:60px;
    background:radial-gradient(ellipse at 50% 50%,rgba(120,170,50,.75) 0%,rgba(200,90,60,.5) 55%,rgba(243,244,243,0) 78%);}
  .title-box{position:absolute;left:116px;top:177px;width:328px;height:470px;background:var(--box);overflow:hidden;}
  .front-title{position:absolute;left:20px;top:30px;margin:0;font-family:'Archivo Black',sans-serif;
    font-size:58px;line-height:100px;color:var(--green);letter-spacing:-.5px;}
  .front-subtitle{position:absolute;left:20px;top:262px;margin:0;width:300px;
    font-size:31px;font-weight:400;line-height:41px;color:var(--light);letter-spacing:.5px;}
  .band{position:absolute;left:0;top:780px;width:552px;height:97px;background:var(--green);}
  .band p{margin:0;position:absolute;left:25px;top:11px;width:512px;
    font-family:'Roboto Condensed',sans-serif;font-size:19.5px;line-height:25px;color:var(--white);letter-spacing:-.2px;}
</style>
</head>
<body>
<div class="wrap">

  <section class="back">
    <div class="fruit-top" role="img" aria-label="Foto: Obst wie Trauben, Äpfel, Himbeeren und Birnen am oberen Rand"></div>
    <h2 class="back-title">MORGENLICHT</h2>
    <h3 class="back-subtitle">FINDE RUHE DURCH WANDERN<br>UND TAGTRÄUMEN</h3>
    <div class="blurb">
      <p>Bist du auf der Suche nach mehr Wohlbefinden und möchtest deine Gesundheit nachhaltig verbessern? Suchst du nach Methoden deinen Körper von Schadstoffen zu befreien, die dich in der Vergangenheit belastet haben? Möglicherweise fragst du dich warum das so ist und was es damit auf sich hat?</p>
      <p>Detox, Entschlacken und Entgiften, Diäten und eine gesündere Ernährungsweise ist in aller Munde. Der Grund dafür ist bei zahlreichen Menschen ein mangelndes Wohlbefinden durch zivillisationsbedingte Einflüsse wie Umweltverschmutzungen, Stress und eine unbewusste Ernährungsweise. Diese Faktoren führen zu krankhaften Symptomen, Energie- und Antriebs&shy;losigkeit und letztendlich zu den steigenden Zahlen überge&shy;wichtiger Menschen in unserer Bevölkerung.</p>
      <p>In diesem Ratgeber erfährst du, wie wichtig es ist sich zu entgiften und wie wichtig dafür eine gesunde Ernährungs&shy;weise ist. Zusätzlich erfährst du, wie du praktische Heil&shy;methoden anwendest, die die Darmgesundheit wiederherstellen und wie du die Entgiftung in den einzelnen Bereichen des Körpers vorantreibst. Denn Detox ist heutzutage wichtiger denn je!</p>
    </div>
    <div class="fruit-bottom" role="img" aria-label="Foto: Gemüse wie Auberginen, Kohl, Spargel, Mais, Karotten und Paprika am unteren Rand"></div>
  </section>

  <section class="spine">
    <div class="spine-text">LUKAS FERNDAHL&nbsp;&nbsp;- <span class="spine-title">MORGENLICHT - FINDE RUHE DURCH WANDERN UND TAGTRÄUMEN</span></div>
  </section>

  <section class="front">
    <p class="author">LUKAS FERNDAHL</p>
    <div class="produce" role="img" aria-label="Foto: frisches Gemüse und Obst rund um den Titel – Tomaten, Paprika, Erdbeeren, Zitrone, Apfel, Brokkoli, Gurke, Knoblauch"></div>
    <div class="title-box" role="img" aria-label="Dunkle Titelfläche mit angedeutetem Darmmotiv im Hintergrund">
      <h1 class="front-title">MORGEN<br>LICHT</h1>
      <h2 class="front-subtitle">FINDE RUHE DURCH WANDERN UND TAGTRÄUMEN</h2>
    </div>
    <div class="band">
      <p>Durch Entgiften und Entschlacken das Wohlbefinden steigern, die Darmgesundheit wieder herstellen, das Gewicht reduzieren und die Heilung für Körper und Geist einleiten</p>
    </div>
  </section>

</div>
</body>
</html>
```